Website for Youth Orchestra to sell tickets and attract young musicians

We are looking for a new website design for a Youth Orchestra; one of the best classical youth orchestras in the county. This project is the design only. <br/><br/>The website serves two main purposes:<br/>• Selling tickets for concerts and performances of the orchestra<br/>• Recruiting young musicians to do audition for the orchestra<br/>
Updates

Target Market(s)

Classical music lovers with a special interest in young upcoming musicians.
Young talented musicians

Number of Pages Required

2 page

Colors
ec1f27

Requirements
Must have
• - A Picture on the front page that promotes the main upcomming event
• - Attention for recruiting new musicians
• - Pictures with young musicians (white back ground, see examples)
• - Responsive
• - Please use the logo attached
Should not have
• The brown colors of the current website (kvb-veldhorst.example)

```html
<!DOCTYPE html>
<html lang="nl">
<head>
<meta charset="utf-8">
<title>Veldhorst Jeugdorkest</title>
<link href="https://fonts.googleapis.com/css2?family=Comfortaa:wght@400;600;700&display=swap" rel="stylesheet">
<style>
  :root {
    --red: #ea3541;
    --orange: #ef7b22;
    --white: #ffffff;
    --ink: #1a1414;
  }
  * { margin: 0; padding: 0; box-sizing: border-box; }
  html, body { width: 1200px; height: 675px; overflow: hidden; }
  body {
    position: relative;
    font-family: "Comfortaa", sans-serif;
    color: var(--white);
    background: var(--orange);
  }
  .stage {
    position: absolute; left: 0; top: 0;
    width: 1000px; height: 675px;
    background: var(--red);
  }
  .brand {
    position: absolute; left: 19px; top: 18px;
    width: 112px;
    font-size: 17px; font-weight: 700; line-height: 1.05;
    display: flex; align-items: center; gap: 6px;
  }
  .brand-mark { width: 10px; height: 10px; background: var(--white); flex: none; }
  .main-nav {
    position: absolute; left: 152px; top: 37px;
    display: flex; gap: 25px;
    font-size: 13.5px; letter-spacing: 0.3px;
  }
  .main-nav a { color: var(--white); text-decoration: none; }
  .main-nav a.active { font-weight: 700; position: relative; }
  .main-nav a.active::after {
    content: ""; position: absolute; left: 0; top: 20px;
    width: 25px; height: 1.5px; background: var(--white);
  }
  .headline {
    position: absolute; left: 0; top: 154px; width: 1000px;
    text-align: center; font-size: 25px; font-weight: 700; letter-spacing: 0.8px;
  }
  .event-title {
    position: absolute; left: 25px; top: 271px;
    font-size: 17px; font-weight: 700; letter-spacing: 0.6px;
  }
  .event-photo {
    position: absolute; left: 117px; top: 322px;
    width: 352px; height: 185px; border-radius: 10px;
    background: linear-gradient(180deg, #c9884a 0%, #8a5a2e 45%, #3a2a22 100%);
  }
  .btn {
    position: absolute; top: 535px; height: 34px; width: 144px;
    border-radius: 3px; font-size: 14px; font-weight: 700; letter-spacing: 0.6px;
    display: flex; align-items: center; justify-content: center;
    color: var(--white); text-decoration: none;
  }
  .btn-buy { left: 140px; background: var(--orange); }
  .btn-info { left: 302px; border: 2px solid var(--orange); }
  .events-note {
    position: absolute; left: 119px; top: 596px;
    font-size: 18px; letter-spacing: 0.6px;
  }
  .events-note a { color: var(--orange); font-weight: 700; }
  .soloist {
    position: absolute; left: 530px; top: 262px;
    width: 400px; height: 413px;
    background: radial-gradient(ellipse at 50% 35%, #e9c6a0 0%, #b98a5c 30%, #3a2622 60%, rgba(26,20,20,0.9) 80%);
    border-radius: 45% 45% 0 0;
  }
  .slider-btn {
    position: absolute; top: 593px; width: 62px; height: 62px;
    border: 2px solid var(--white);
  }
  .slider-prev { left: 925px; opacity: 0.35; }
  .slider-next { left: 1012px; }
  .slider-btn svg { width: 100%; height: 100%; }
</style>
</head>
<body>
  <div class="stage"></div>

  <div class="brand"><span class="brand-mark"></span><span>Veldhorst Jeugdorkest</span></div>

  <nav class="main-nav">
    <a class="active" href="#">Home</a>
    <a href="#">Orkest</a>
    <a href="#">Speel Mee</a>
    <a href="#">Concerten</a>
    <a href="#">Tournees</a>
    <a href="#">Partners</a>
    <a href="#">Vrienden</a>
    <a href="#">Oudleden</a>
    <a href="#">Contact &amp; Organisatie</a>
  </nav>

  <h1 class="headline">The biggest Youth Orchestra of the Country!</h1>

  <h2 class="event-title">Kaartverkoop vjo nieuwjaarsconcert 12 januari 2020 gestart!</h2>

  <div class="event-photo" role="img" aria-label="Orchestra performing on stage in a full concert hall"></div>

  <a class="btn btn-buy" href="#">Buy Ticket</a>
  <a class="btn btn-info" href="#">More Info</a>

  <p class="events-note">For all our upcoming events click <a href="#">here</a></p>

  <div class="soloist" role="img" aria-label="Young violinist playing, cut out against the red background"></div>

  <div class="slider-btn slider-prev">
    <svg viewBox="0 0 62 62"><polyline points="36,18 22,31 36,44" fill="none" stroke="#fff" stroke-width="1.5"/></svg>
  </div>
  <div class="slider-btn slider-next">
    <svg viewBox="0 0 62 62"><polyline points="26,18 40,31 26,44" fill="none" stroke="#fff" stroke-width="1.5"/></svg>
  </div>
</body>
</html>
```